Lorvena Aesthetic Doctor

I require an elegant, luxurious looking business card for my aesthetic business. I am a doctor and that will set me aside from competitors. I am planning to provide home and spa based treatments to clients with high expectations. I have attached my logo.

```html
<!DOCTYPE html>
<html lang="en">
<head>
<meta charset="utf-8">
<title>Lorvena Aesthetic Doctor – Business Card</title>
<link rel="stylesheet" href="https://fonts.googleapis.com/css2?family=Marcellus&family=Roboto:ital,wght@0,300;0,400;1,400&family=Montserrat:wght@500&display=swap">
<style>
  :root {
    --page-bg: #d9dadc;
    --blue-light: #5db3e3;
    --blue-deep: #1769b0;
    --blue-accent: #3a9fd8;
    --silver: #dfe3e7;
    --silver-dark: #b9bec4;
    --card-white: #f4f5f6;
    --wave-grey: #9aa2ae;
    --ink: #2f3338;
  }
  * { box-sizing: border-box; margin: 0; padding: 0; }
  html, body { width: 1200px; height: 576px; overflow: hidden; }
  body { background: var(--page-bg); position: relative; font-family: "Roboto", Arial, sans-serif; }

  .card {
    position: absolute; top: 138px; height: 294px; border-radius: 12px; overflow: hidden;
  }

  /* Front */
  .card-front {
    left: 81px; width: 486px;
    background: linear-gradient(160deg, var(--blue-light) 0%, #2f86c8 55%, var(--blue-deep) 100%);
  }
  .brand-mark {
    position: absolute; border: 2px solid var(--silver); border-radius: 50%;
  }
  .card-front .brand-mark { left: 45px; top: 36px; width: 124px; height: 124px; }
  .brand-name {
    position: absolute; font-family: "Marcellus", Georgia, serif; font-weight: 400; line-height: 1;
  }
  .brand-name .line-main { display: block; letter-spacing: 2px; }
  .brand-name .line-sub { display: block; letter-spacing: 1.5px; margin-top: 6px; }
  .card-front .brand-name { left: 190px; top: 64px; color: var(--silver); }
  .card-front .line-main { font-size: 46px; }
  .card-front .line-sub { font-size: 19px; }

  .service-list {
    position: absolute; left: 0; right: 0; top: 196px; text-align: center;
    color: #eaf4fb; font-size: 13.5px; font-weight: 400; line-height: 18px;
  }
  .service-list .sep { margin: 0 8px; }
  .treatment-band {
    position: absolute; left: 0; right: 0; top: 245px; height: 23px;
    background: linear-gradient(180deg, #c9ced3 0%, #eef0f2 45%, #b7bcc2 100%);
    text-align: center; font-family: "Montserrat", Arial, sans-serif; font-weight: 500;
    font-size: 12.5px; letter-spacing: 0.6px; line-height: 23px; color: #1e2228;
  }

  /* Back */
  .card-back { left: 602px; width: 481px; height: 291px; background: var(--card-white); }
  .card-back .wave { position: absolute; left: 0; top: 0; }
  .tagline {
    position: absolute; left: 26px; top: 22px; color: #ffffff;
    font-size: 13px; font-weight: 300; line-height: 17px;
  }
  .card-back .brand-mark { left: 176px; top: 86px; width: 80px; height: 80px; border-color: var(--blue-accent); }
  .card-back .brand-name { right: 27px; top: 96px; color: var(--blue-accent); text-align: right; }
  .card-back .line-main { font-size: 36px; }
  .card-back .line-sub { font-size: 16px; margin-top: 5px; }

  .social { position: absolute; left: 26px; top: 181px; font-size: 12.5px; color: var(--ink); display: flex; align-items: center; }
  .social .dot { width: 11px; height: 11px; border-radius: 50%; background: var(--blue-accent); margin-left: 5px; }
  .social .dot:first-of-type { margin-left: 8px; }
  .contact-list { position: absolute; left: 26px; top: 209px; list-style: none; font-size: 12.5px; color: var(--ink); }
  .contact-list li { display: flex; align-items: center; height: 18.5px; }
  .contact-list svg { width: 10px; height: 10px; margin: 0 10px 0 4px; fill: var(--blue-accent); }

  .doctor { position: absolute; right: 27px; top: 187px; text-align: right; }
  .doctor-name { font-size: 18.5px; font-weight: 300; color: var(--ink); }
  .doctor-postnominals { font-size: 10px; font-style: italic; color: var(--blue-accent); margin-top: 2px; }
  .doctor-diploma { font-size: 12.5px; color: var(--blue-accent); margin-top: 8px; line-height: 16px; }
</style>
</head>
<body>
  <section class="card card-front" aria-label="Business card front">
    <div class="brand-mark"></div>
    <div class="brand-name">
      <span class="line-main">LORVENA</span>
      <span class="line-sub">AESTHETIC DOCTOR</span>
    </div>
    <p class="service-list">
      Dermal Injectables<span class="sep">|</span>Plasma Facials<span class="sep">|</span>Microneedling<br>
      Skin Boosters<span class="sep">|</span>Excessive Sweating
    </p>
    <div class="treatment-band">HOME AND SPA BASED TREATMENTS</div>
  </section>

  <section class="card card-back" aria-label="Business card back">
    <svg class="wave" width="481" height="130" viewBox="0 0 481 130" aria-hidden="true">
      <path d="M0 0H481V22C400 10 330 22 262 60C192 98 92 100 0 72Z" fill="var(--blue-accent)" opacity="0.9"/>
      <path d="M0 82C95 112 200 104 272 64C344 26 420 14 481 26V34C420 24 350 36 280 74C206 114 92 120 0 92Z" fill="var(--wave-grey)"/>
      <path d="M230 40C300 16 380 8 470 18" stroke="var(--wave-grey)" stroke-width="3" fill="none" opacity="0.7"/>
    </svg>
    <p class="tagline">Home and Spa<br>Based Treatments</p>

    <div class="brand-mark"></div>
    <div class="brand-name">
      <span class="line-main">LORVENA</span>
      <span class="line-sub">AESTHETIC DOCTOR</span>
    </div>

    <div class="social">Follow us on:<span class="dot"></span><span class="dot"></span></div>
    <ul class="contact-list">
      <li><svg viewBox="0 0 10 10"><path d="M2 0.5L3.6 2.6 2.8 3.6C3.4 5 4.8 6.4 6.3 7.1L7.3 6.3 9.5 7.9 8.6 9.5C4.4 9.3 0.6 5.5 0.5 1.4Z"/></svg>0800 555 019</li>
      <li><svg viewBox="0 0 10 10"><path d="M0 2H10V8H0ZM0.8 2.6L5 5.6 9.2 2.6V3.4L5 6.4 0.8 3.4Z" fill-rule="evenodd"/></svg>mirela@lorvena.co.nz</li>
      <li><svg viewBox="0 0 10 10"><path d="M5 0A5 5 0 1 0 5 10A5 5 0 1 0 5 0ZM1 4.5H3A8 8 0 0 1 4.5 1.1 4 4 0 0 0 1 4.5ZM5.5 1.1A8 8 0 0 1 7 4.5H9A4 4 0 0 0 5.5 1.1ZM4 4.5H6A7 7 0 0 0 5 1.5 7 7 0 0 0 4 4.5ZM1 5.5A4 4 0 0 0 4.5 8.9 8 8 0 0 1 3 5.5ZM4 5.5A7 7 0 0 0 5 8.5 7 7 0 0 0 6 5.5ZM7 5.5A8 8 0 0 1 5.5 8.9 4 4 0 0 0 9 5.5Z" fill-rule="evenodd"/></svg>www.lorvena.co.nz</li>
    </ul>

    <div class="doctor">
      <p class="doctor-name">Dr Mirela Vostak</p>
      <p class="doctor-postnominals">MRCPCH MD</p>
      <p class="doctor-diploma">Australasian Diploma of<br>Aesthetic Medicine</p>
    </div>
  </section>
</body>
</html>
```